Interactive Children's Media Book Company Website Design

We need a website DESIGN (no coding required) for a new interactive children's media book company called Tovira Studios.

We develop high-quality interactive children's books for the Lumo Tab/Lumo Phone that seeks to delight and inspire young and old alike. Our stories are filled with heart and spirit, and we seek to breathe magic back into books so that people fall back in love with reading.

Tovira means "butterfly" in Korean. It plays on the idea that a caterpillar metamorphoses into a butterfly - and in the same way, our readers are transformed through the journey of experiencing our interactive books.

We're looking for something based on the ATTACHED LOGO DESIGN for our company. A website that's professional, modern, fun and inviting; easy to read and not-cluttered, but still portraying the feeling of innocence and childhood.

We're looking for something that resonates the magical experience we want to create for our readers. Specific requirements on pages, tabs, content, etc are below.

• There are 7 tabs on the Homepage of the website: HOME, OUR GRANDPA, ABOUT US, CAREERS, NEWS, CONTACT US, SHOP. (But there is an extra page called YOUR GRANDPA, which will be a sub-page under Our Grandpa).

HOME
• Would be great to have some key images of our book (3-4 screen shots) as the key focus of the homepage that automatically scroll through every few seconds. (Placeholder image attached). The images would link to the “Our Grandpa” page.
• Company logo (attached to brief) and slogan: “A new era of children’s media” quite prominent on page.
• Key text content to be on page: “Tovira means “butterfly” in Korean. Just as a caterpillar transforms into a butterfly, Tovira Studios takes the reader on an unforgettable journey of metamorphosis through our stories. We turn children’s books into a high-quality interactive experience on mobile platforms - breathing magic back into books, and inspiring people to fall back in love with reading. Through our unique characters full of heart and spirit, our stories delight and inspire young and old alike.”
• plain square & plain square Like & plain square page link icons.
• Section on Latest News with a few of the latest entries.
• Section on latest sister images & comments that visitors have posted, which takes you to the “Your Grandpa” page.

OUR GRANDPA
• The title for this page is “Our Grandpa Hums at Breakfast Time”
• There will be a little Lumo Tab/Lumo Phone icon (placeholder attached) for this book.
• There will be a link to the plain badge to buy the app book.
• Key text content on this page: “Our debut interactive media book is coming soon on the Lumo Tab and Lumo Phone! “Our Grandpa Hums at Breakfast Time” touches on the beautiful and inextricable (albeit sometimes frustrating!) bond between sisters.”
• There will be a section on “Features” which lists all the various special features the app book includes.
• There will be a YouTube clip embedded into the page, which shows how the app book works.
• A section that says: “Do you have a sister who’s not like other sisters? Share a photo and tell us about her!” which links to the sub-page “Your Grandpa”.
• Under this, there may be the most recent few images submitted by the public, which when clicked on, would also link to the sub-page “Your Grandpa”.

YOUR GRANDPA
• The main text on the page: “Do you have a sister who’s not like other sisters? Share a photo and tell us about her!”
• Main body of the page is a gallery of all the photos that have been submitted. If you click on each of the images, you get the comments that people have submitted with the photos.
• The page would also have a Submit Comments Form, where people can upload a picture of their sister(s) and write a comment to accompany the image.

ABOUT US
• Introductory text on page: “It was a chance conversation at Harbourline Terminal, where two friends discovered they shared a dream to create quality children's media. Both of them were excited by the possibilities of using new digital platforms to inspire and educate a younger generation. From that idea Tovira Studios was born. We seek to be the chrysalis of story telling - to inspire the hearts and minds of our generation, and generations to come.”
• Section to “Join the Mailing List” where they can put their email address in and submit.
• Bios of 2x people with photos (bios in word doc attached) (do not have photos yet).

CAREERS
• The main text on the page: “We are always on the lookout for talented people to join our team. If you are a writer, illustrator, animator, iOS/android developer, musician, creative-writing translator - or have something special to offer Tovira Studios - we are keen to hear from you. Send us a message through the Contact Us tab above.”

NEWS
• Regular News page, with blog-type entries.

CONTACT US
• Online submit Contact Us form
• The main text on page: “Our studio is based in the Ember Craft Cooperative, 43 Pukeora Street, Marangai, Wellington. Ember is a professional, creative collective - with four separate studios, gallery, and retail store. For more information on Ember, visit: http://www.embercraftco.example.nz”
• “We would love to hear from you! Whether you have questions, ideas, comments, or just want to say hullo - please leave us a message and we will get back to you soon.”
• Including image of the premises (Ember image attached to brief).

SHOP
• Where visitors can purchase merchandise (t-shirts, mugs, etc) of the book/company.

```html
<!DOCTYPE html>
<html lang="en">
<head>
<meta charset="utf-8">
<title>Tovira Studios – Our Grandpa Hums at Breakfast Time</title>
<link rel="stylesheet" href="https://fonts.googleapis.com/css2?family=Questrial&family=Fredoka:wght@500&family=Arimo:wght@400;700&display=swap">
<style>
:root{
  --page-top:#fbf3fb;
  --page-bottom:#ece8fb;
  --panel:#ffffff;
  --panel-edge:#dcd8e4;
  --nav-top:#72b8f2;
  --nav-bottom:#9a68ee;
  --slogan:#8c8c8c;
  --logo:#a28fd8;
  --title:#7566e0;
  --feature-title:#b45ee6;
  --body:#4a4a4a;
  --heading:#4f4f4f;
  --box-edge:#d6d6d6;
  --box-fill:#f2f2f2;
  --thumb-label:#c4c4c4;
  --share-top:#4cb8ee;
  --share-bottom:#a66ae6;
  --footer-line:#8a8a8a;
}
*{box-sizing:border-box;margin:0;padding:0}
html,body{width:1200px;height:1029px;overflow:hidden}
body{
  position:relative;
  font-family:"Arimo",sans-serif;
  background:linear-gradient(160deg,var(--page-top) 0%,#f4effb 50%,var(--page-bottom) 100%);
}
.abs{position:absolute}

/* header */
.brand{left:120px;top:30px;display:flex;align-items:center;gap:14px}
.brand-dot{width:60px;height:60px;border-radius:50%;background:var(--logo)}
.brand-name{font-family:"Questrial",sans-serif;font-size:40px;color:var(--logo);line-height:1}
.slogan{left:459px;top:14px;font-family:"Questrial",sans-serif;font-size:29px;color:var(--slogan);letter-spacing:.2px}
.social{top:16px;width:25px;height:25px;border-radius:3px}
.social-a{left:1023px;background:#4a66a8}
.social-b{left:1054px;background:#4fbde8}

.nav{
  left:454px;top:61px;width:625px;height:50px;border-radius:9px;
  background:linear-gradient(180deg,var(--nav-top) 0%,#8c8cf0 55%,var(--nav-bottom) 100%);
  box-shadow:0 1px 3px rgba(120,100,180,.35);
  display:flex;align-items:center;padding-left:26px;
}
.nav a{
  font-family:"Arimo",sans-serif;font-size:13px;color:#fff;text-decoration:none;
  margin-right:30px;letter-spacing:.2px;
}
.nav a.active{
  background:linear-gradient(#fff,#e6e6e6);color:#222;border-radius:11px;
  padding:4px 13px;margin-left:-13px;margin-right:17px;
}

/* content panel */
.panel{
  left:120px;top:133px;width:960px;height:842px;background:var(--panel);
  border-radius:13px;border:1px solid var(--panel-edge);
  box-shadow:0 0 5px rgba(140,120,180,.3);
}
.page-title{left:141px;top:155px;font-size:22px;color:var(--title);font-weight:400}
.intro{left:141px;top:195px;width:650px;font-size:11px;line-height:19px;color:var(--body)}
.store-badge{left:142px;top:251px;width:145px;height:49px;border-radius:5px;background:#0c0c0c;border:1px solid #999}
.devices{left:816px;top:150px;width:236px;height:234px;border-radius:14px;
  background:linear-gradient(135deg,#3a3a3a 0%,#e0743c 45%,#46b4dc 100%)}

.features-heading{left:141px;top:381px;font-size:19px;color:var(--heading);font-weight:400}
.feature{
  left:141px;width:655px;height:175px;border:1px solid var(--box-edge);border-radius:4px;
  background:linear-gradient(180deg,#fff 0%,var(--box-fill) 100%);
}
.feature h3{position:absolute;left:16px;top:13px;font-size:13px;font-weight:700;color:var(--feature-title)}
.feature p{position:absolute;left:150px;top:33px;width:493px;font-size:11.2px;line-height:18.8px;color:var(--body)}
.thumb{
  position:absolute;background:#fff;border:1px solid #c8c8c8;border-radius:3px;
  display:flex;align-items:center;justify-content:center;overflow:hidden;
}
.thumb span{font-size:17px;color:var(--thumb-label);transform:rotate(-26deg);letter-spacing:.5px}
.feature .thumb{left:18px;top:36px;width:119px;height:96px}

.video{left:817px;top:409px;width:235px;height:174px;background:#000;border:3px solid #fff;outline:1px solid #d4d4d4}
.video-frame{position:absolute;left:72px;top:34px;width:84px;height:110px;border-radius:4px;background:#1c1c1c;border:1px solid #333}
.video-play{position:absolute;left:89px;top:61px}

.share{
  left:817px;top:597px;width:235px;height:364px;border-radius:5px;border:1px solid #d8d0ee;
  background:linear-gradient(180deg,var(--share-top) 0%,#8a8cf0 50%,var(--share-bottom) 100%);
}
.share p{
  position:absolute;left:0;top:12px;width:235px;text-align:center;
  font-family:"Fredoka",sans-serif;font-weight:500;font-size:22px;line-height:28px;color:#fff;
  text-shadow:0 1px 2px rgba(60,40,120,.45);
}
.share .thumb{width:90px;height:77px;border-color:#dcd6f0}
.share .thumb span{font-size:13px}

.footer-line{left:124px;top:990px;width:951px;height:1px;background:var(--footer-line)}
.copyright{left:0;top:998px;width:1200px;text-align:center;font-size:10.5px;color:#222}
</style>
</head>
<body>

<header>
  <div class="abs brand"><span class="brand-dot"></span><span class="brand-name">Tovira Studios</span></div>
  <div class="abs slogan">A new era of children’s media...</div>
  <a class="abs social social-a" href="#" aria-label="Social page one"></a>
  <a class="abs social social-b" href="#" aria-label="Social page two"></a>
  <nav class="abs nav">
    <a href="#">HOME</a>
    <a href="#" class="active">OUR GRANDPA</a>
    <a href="#">ABOUT US</a>
    <a href="#">CAREERS</a>
    <a href="#">NEWS</a>
    <a href="#">CONTACT US</a>
    <a href="#">SHOP</a>
  </nav>
</header>

<main>
  <div class="abs panel"></div>

  <h1 class="abs page-title">Our Grandpa Hums at Breakfast Time</h1>
  <p class="abs intro">Our debut interactive media book is coming soon on the Lumo Tab and Lumo Phone! "Our Grandpa Hums at Breakfast Time" touches on the beautiful and inextricable (albeit sometimes frustrating!) bond between sisters.</p>
  <a class="abs store-badge" href="#" aria-label="Get the app book"></a>
  <div class="abs devices" role="img" aria-label="Tablet and phone showing the book’s cover character"></div>

  <h2 class="abs features-heading">Features</h2>

  <section class="abs feature" style="top:409px">
    <h3>Feature 1</h3>
    <div class="thumb"><span>THUMBNAIL</span></div>
    <p>Lorem ipsum dolor sit amet consecutor. Lorem ipsum dolor sit amet consecutor. Lorem ipsum dolor sit amet consecutor. Lorem ipsum dolor sit amet consecutor. Lorem ipsum dolor sit amet consecutor. Lorem ipsum dolor sit amet consecutor. Lorem ipsum dolor sit amet consecutor. Lorem ipsum dolor sit amet consecutor. Lorem ipsum dolor sit amet consecutor. Lorem ipsum dolor sit amet consecutor. Lorem ipsum dolor sit amet consecutor. Lorem ipsum dolor sit amet consecutor. Lorem ipsum dolor sit amet .</p>
  </section>
  <section class="abs feature" style="top:597px">
    <h3>Feature 2</h3>
    <div class="thumb"><span>THUMBNAIL</span></div>
    <p>Lorem ipsum dolor sit amet consecutor. Lorem ipsum dolor sit amet consecutor. Lorem ipsum dolor sit amet consecutor. Lorem ipsum dolor sit amet consecutor. Lorem ipsum dolor sit amet consecutor. Lorem ipsum dolor sit amet consecutor. Lorem ipsum dolor sit amet consecutor. Lorem ipsum dolor sit amet consecutor. Lorem ipsum dolor sit amet consecutor. Lorem ipsum dolor sit amet consecutor. Lorem ipsum dolor sit amet consecutor. Lorem ipsum dolor sit amet consecutor. Lorem ipsum dolor sit amet .</p>
  </section>
  <section class="abs feature" style="top:787px">
    <h3>Feature 3</h3>
    <div class="thumb"><span>THUMBNAIL</span></div>
    <p>Lorem ipsum dolor sit amet consecutor. Lorem ipsum dolor sit amet consecutor. Lorem ipsum dolor sit amet consecutor. Lorem ipsum dolor sit amet consecutor. Lorem ipsum dolor sit amet consecutor. Lorem ipsum dolor sit amet consecutor. Lorem ipsum dolor sit amet consecutor. Lorem ipsum dolor sit amet consecutor. Lorem ipsum dolor sit amet consecutor. Lorem ipsum dolor sit amet consecutor. Lorem ipsum dolor sit amet consecutor. Lorem ipsum dolor sit amet consecutor. Lorem ipsum dolor sit amet .</p>
  </section>

  <div class="abs video" aria-label="Video showing how the app book works">
    <div class="video-frame" role="img" aria-label="Video still of the book"></div>
    <svg class="video-play" width="52" height="52" viewBox="0 0 52 52" aria-hidden="true">
      <circle cx="26" cy="26" r="23" fill="rgba(40,40,40,.7)" stroke="#bbb" stroke-width="3"/>
      <path d="M20 16 L36 26 L20 36 Z" fill="#fff"/>
    </svg>
  </div>

  <aside class="abs share">
    <p>Do you have a<br>sister who’s not<br>like other sisters?<br>Share a photo and<br>tell us about her!</p>
    <svg class="abs" style="left:111px;top:169px" width="14" height="12" viewBox="0 0 14 12" aria-hidden="true"><path d="M2 10 L7 4 L12 10" fill="none" stroke="#fff" stroke-width="3"/></svg>
    <div class="thumb" style="left:17px;top:186px"><span>THUMBNAIL</span></div>
    <div class="thumb" style="left:127px;top:186px"><span>THUMBNAIL</span></div>
    <div class="thumb" style="left:17px;top:277px"><span>THUMBNAIL</span></div>
    <div class="thumb" style="left:127px;top:277px"><span>THUMBNAIL</span></div>
    <svg class="abs" style="left:111px;top:346px" width="14" height="12" viewBox="0 0 14 12" aria-hidden="true"><path d="M2 2 L7 8 L12 2" fill="none" stroke="#fff" stroke-width="3"/></svg>
  </aside>
</main>

<footer>
  <div class="abs footer-line"></div>
  <p class="abs copyright">Copyright © 2011 tovira. All Rights Reserved</p>
</footer>

</body>
</html>
```